Web portal for events

The project is about creating a web application - portal for culture events in Denmark.

Design

We aim for very simplistic, light and fully responsive design. The white background is preferable, as well as light color tones. As inspirational points we like the colors used in www.brimtok.com and www.velmorastay.org

FORMAT AND REQUIREMENTS:
1. Design should be provided based on the wireframes specified as a link below.
2. The design (and all of its pages) should be provided in three resolution variants:
- Desktop
- Tablet
- Phone
3. The design should be provided as PSD, where each page/section should be in its own PSD file
4. All graphical elements in the design should be delivered as single layers which can then be extracted from the PSD.
5. All graphical elements (icons, graphical buttons, etc.) should be provided as vector objects in the PSD, so that they can be exported into different sizes without loss of quality (for responsiveness)
6. The design should use either web safe fonts or Google Fonts.

RESPONSIVENESS
The web application should be visible on any devices (i.e. responsive design)

WIREFRAMES:
https://tessalquin.wirebox.example/projects/eventhall/prototype/Homepage?key=b3c7d1e9f2a4068c5e7b9d1f3a5c7e9b2d4f6a80

We expect design of the following wireframes:

Homepage:
https://tessalquin.wirebox.example/projects/eventhall/Homepage

For arrangører - billede uploaded:
https://tessalquin.wirebox.example/projects/eventhall/For%20arrang%C3%B8rer%20-%20billede%20uploaded

Further specifications of the project (i.e. functionality, etc.):
https://papers.plorvex.example/document/d/9qRt_Lm3NvXpZ8wKjHs2AbCdEfGh7iJkLmNoPq4rSt/edit?usp=sharing

```html
<!DOCTYPE html>
<html lang="da">
<head>
<meta charset="utf-8">
<title>KULTRA – Din guide til kultur og events</title>
<link href="https://fonts.googleapis.com/css2?family=Arimo:ital,wght@0,400;0,700;1,400;1,700&display=swap" rel="stylesheet">
<style>
:root{
  --navy:#1b2245;
  --navy-dark:#141a36;
  --orange:#d35400;
  --orange-line:#b94a00;
  --text:#1b2245;
  --muted:#777;
  --light:#c8c8c8;
  --rule:#e3e3e3;
  --footer:#e2e2e2;
}
*{box-sizing:border-box;margin:0;padding:0}
html,body{width:1200px;height:1075px;overflow:hidden;background:#fff;font-family:"Arimo",Arial,sans-serif;color:var(--text)}
.page{position:relative;width:1200px;height:1075px}
.abs{position:absolute}

/* header */
.site-header{position:absolute;left:0;top:0;width:1200px;height:126px;background:var(--navy)}
.brand{position:absolute;left:124px;top:16px;color:#fff}
.brand-name{font-size:64px;font-weight:400;letter-spacing:2px;line-height:64px}
.brand-tag{font-size:12px;margin-top:6px}
.account{position:absolute;top:21px;right:125px;display:flex;gap:26px;color:#e6e6e6;font-weight:700;font-size:15px}
.account span{display:flex;align-items:center;gap:8px}
.search{position:absolute;left:645px;top:67px;width:253px;height:36px;display:flex}
.search input{width:216px;height:36px;border:0;background:#2c3458;color:#aab;padding-left:14px;font:15px "Arimo",sans-serif}
.search button{width:37px;height:36px;border:0;background:var(--navy-dark);display:flex;align-items:center;justify-content:center}
.adv-search{position:absolute;left:905px;top:67px;width:170px;height:36px;background:var(--orange);color:#fff;font-weight:700;font-size:15px;display:flex;align-items:center;justify-content:center}

/* nav */
.main-nav{position:absolute;left:0;top:126px;width:1200px;height:58px;background:var(--orange)}
.main-nav a{position:absolute;top:0;height:58px;line-height:58px;text-align:center;color:#f6c9a6;font-size:17px;text-decoration:none;border-left:1px solid var(--orange-line)}
.main-nav a.active{background:var(--navy);color:#fff;border:0}
.nav-shadow{position:absolute;left:135px;top:184px;width:935px;height:24px;background:radial-gradient(ellipse at 50% 0,rgba(0,0,0,.22),rgba(0,0,0,0) 70%)}

/* headings */
.section-title{position:absolute;font-size:21px;font-weight:700;color:var(--navy)}
.section-title::after{content:"";position:absolute;left:0;top:32px;width:148px;height:4px;background:var(--light)}

.sort{position:absolute;left:449px;top:221px;display:flex;align-items:center;gap:5px;font-size:13px}
.sort-label{font-size:16px;font-weight:700;margin-right:3px}
.sort .opt{height:26px;line-height:24px;border:1px solid #ccc;padding:0 11px;color:#555}
.sort .opt.on{background:var(--orange);border-color:var(--orange);color:#fff}
.sort .select{display:flex;padding:0 0 0 11px}
.sort .select i{display:block;width:22px;height:24px;background:#ccc;margin-left:10px;position:relative}
.sort .select i::after{content:"";position:absolute;left:7px;top:10px;border:4px solid transparent;border-top-color:#fff}

/* cards */
.event-card{position:absolute;width:208px}
.event-photo{position:relative;width:208px;height:108px}
.date-badge{position:absolute;left:0;bottom:0;width:43px;height:46px;background:var(--navy);color:#fff;text-align:center}
.date-badge b{display:block;font-style:italic;font-size:19px;line-height:22px;margin-top:5px}
.date-badge small{display:block;font-size:12px;line-height:12px}
.event-title{font-size:16px;font-weight:700;margin-top:14px;letter-spacing:.2px}
.event-desc{font-size:13.5px;color:var(--muted);line-height:20px;margin-top:6px}
.event-foot{display:flex;justify-content:space-between;align-items:center;margin-top:10px;width:178px}
.btn-event{display:inline-block;width:69px;height:20px;line-height:20px;text-align:center;font-size:12px;background:var(--light);color:#555}
.btn-event.on{background:var(--navy);color:#fff}
.likes{display:flex;align-items:center;gap:4px;font-size:14px;color:#888}

.divider{position:absolute;left:823px;top:221px;width:1px;height:759px;background:#ccc}

/* favorites */
.fav{position:absolute;left:847px;width:228px;height:94px;border-bottom:1px solid var(--rule)}
.fav .thumb{position:absolute;left:0;top:0;width:100px;height:65px}
.fav .name{position:absolute;left:111px;top:3px;font-size:14px;line-height:17px;width:115px}
.fav .name.hot{color:var(--orange)}
.fav .date{position:absolute;left:111px;top:47px;font-size:12.5px;color:#999;font-weight:700}

/* newsletter */
.newsletter{position:absolute;left:847px;top:764px;width:228px;height:216px;border:1px solid #ccc}
.nl-head{height:48px;border-bottom:1px solid #ccc;display:flex;align-items:center;gap:12px;padding-left:18px;font-size:21px;font-weight:700}
.nl-text{font-style:italic;font-size:12.5px;line-height:23px;color:#888;padding:11px 20px 0 20px}
.nl-form{position:absolute;left:19px;top:179px;display:flex}
.nl-form input{width:170px;height:28px;border:1px solid var(--navy);font:italic 13px "Arimo",sans-serif;padding-left:9px;color:#888}
.nl-form button{width:28px;height:28px;border:0;background:var(--navy);display:flex;align-items:center;justify-content:center}
.nl-stripe{position:absolute;left:0;bottom:0;width:226px;height:5px;background:repeating-linear-gradient(-55deg,#e05a2a 0 9px,#fff 9px 13px,#4f7fb0 13px 22px,#fff 22px 26px)}

/* footer */
.site-footer{position:absolute;left:0;top:1019px;width:1200px;height:56px;background:var(--footer);font-size:13.5px;color:#777}
.foot-nav{position:absolute;left:126px;top:20px}
.foot-nav a{color:#777;text-decoration:none}
.foot-nav a.active{color:#111}
.foot-nav .sep{margin:0 10px}
.copy{position:absolute;right:125px;top:20px}
</style>
</head>
<body>
<div class="page">

<header class="site-header">
  <div class="brand">
    <div class="brand-name">KULTRA</div>
    <div class="brand-tag">DIN GUIDE TIL KULTUR OG EVENTS</div>
  </div>
  <div class="account">
    <span><svg width="16" height="22" viewBox="0 0 16 22"><path d="M4 9V6a4 4 0 0 1 8 0" fill="none" stroke="#d35400" stroke-width="2"/><circle cx="8" cy="15" r="6" fill="none" stroke="#d35400" stroke-width="2"/><circle cx="8" cy="15" r="1.8" fill="#d35400"/></svg>LOGIN</span>
    <span><svg width="20" height="20" viewBox="0 0 20 20"><circle cx="10" cy="7" r="5" fill="none" stroke="#d35400" stroke-width="1.8"/><path d="M1 19c1-5 5-6 9-6s8 1 9 6z" fill="none" stroke="#d35400" stroke-width="1.8"/></svg>SIGN UP</span>
  </div>
  <form class="search"><input type="text" placeholder="Search"><button type="button" aria-label="Søg"><svg width="22" height="22" viewBox="0 0 22 22"><circle cx="9" cy="9" r="7" fill="none" stroke="#d9dbe5" stroke-width="2.5"/><path d="M14 14l6 6" stroke="#d9dbe5" stroke-width="3"/></svg></button></form>
  <div class="adv-search">ADVANCE SEARCH</div>
</header>

<nav class="main-nav">
  <a class="active" style="left:125px;width:85px">ALLE</a>
  <a style="left:210px;width:98px">MUSIK</a>
  <a style="left:308px;width:101px">SPORT</a>
  <a style="left:409px;width:110px">TEATER</a>
  <a style="left:519px;width:141px">UDSTILLING</a>
  <a style="left:660px;width:101px">ELDER</a>
  <a style="left:761px;width:93px">BORN</a>
  <a style="left:854px;width:97px">MOTIN</a>
  <a style="left:951px;width:116px">DIVERSE</a>
</nav>
<div class="nav-shadow"></div>

<h2 class="section-title" style="left:124px;top:223px">POPULER EVENTS</h2>
<div class="sort">
  <span class="sort-label">Sorter Efter</span>
  <span class="opt on">Populer</span>
  <span class="opt select">Omrade<i></i></span>
  <span class="opt">Dato</span>
  <span class="opt">Pris</span>
</div>

<!-- row 1 -->
<article class="event-card" style="left:124px;top:280px">
  <div class="event-photo" role="img" aria-label="Foto: to mænd ser på et dokument" style="background:linear-gradient(135deg,#d9d4cc,#8a7f74 55%,#2a2a2a)"><div class="date-badge"><b>02</b><small>Aug</small></div></div>
  <h3 class="event-title">Jonas Vennberg Koncert</h3>
  <p class="event-desc">Lorem ipsum dolor sit consectetur adipiscing lorem ispum.</p>
  <div class="event-foot"><span class="btn-event on">Se Event</span><span class="likes"><svg width="18" height="15" viewBox="0 0 18 15"><path d="M9 15L1.5 7.5A4 4 0 0 1 9 2.5a4 4 0 0 1 7.5 5z" fill="#d35400"/></svg>03</span></div>
</article>
<article class="event-card" style="left:357px;top:280px">
  <div class="event-photo" role="img" aria-label="Foto: piger der synger i mikrofon" style="background:linear-gradient(135deg,#e3b7a0,#9b6a8a 50%,#5a3b6a)"><div class="date-badge"><b>02</b><small>Aug</small></div></div>
  <h3 class="event-title">Jonas Vennberg Koncert</h3>
  <p class="event-desc">Lorem ipsum dolor sit consectetur adipiscing lorem ispum.</p>
  <div class="event-foot"><span class="btn-event">Se Event</span><span class="likes"><svg width="18" height="15" viewBox="0 0 18 15"><path d="M9 15L1.5 7.5A4 4 0 0 1 9 2.5a4 4 0 0 1 7.5 5z" fill="#bbb"/></svg>03</span></div>
</article>
<article class="event-card" style="left:590px;top:280px">
  <div class="event-photo" role="img" aria-label="Foto: publikum der rækker hånden op i et klasseværelse" style="background:linear-gradient(135deg,#eef0f3,#b9b3aa 55%,#7a6a58)"><div class="date-badge"><b>02</b><small>Aug</small></div></div>
  <h3 class="event-title">Jonas Vennberg Koncert</h3>
  <p class="event-desc">Lorem ipsum dolor sit consectetur adipiscing lorem ispum.</p>
  <div class="event-foot"><span class="btn-event">Se Event</span><span class="likes"><svg width="18" height="15" viewBox="0 0 18 15"><path d="M9 15L1.5 7.5A4 4 0 0 1 9 2.5a4 4 0 0 1 7.5 5z" fill="#bbb"/></svg>03</span></div>
</article>

<!-- row 2 -->
<article class="event-card" style="left:124px;top:523px">
  <div class="event-photo" role="img" aria-label="Foto: glade festdeltagere" style="background:linear-gradient(135deg,#c0203a,#e8a070 50%,#f1d9b0)"><div class="date-badge"><b>02</b><small>Aug</small></div></div>
  <h3 class="event-title">Jonas Vennberg Koncert</h3>
  <p class="event-desc">Lorem ipsum dolor sit consectetur adipiscing lorem ispum.</p>
  <div class="event-foot"><span class="btn-event">Se Event</span><span class="likes"><svg width="18" height="15" viewBox="0 0 18 15"><path d="M9 15L1.5 7.5A4 4 0 0 1 9 2.5a4 4 0 0 1 7.5 5z" fill="#bbb"/></svg>03</span></div>
</article>
<article class="event-card" style="left:357px;top:523px">
  <div class="event-photo" role="img" aria-label="Foto: catwalk med fotografer" style="background:linear-gradient(135deg,#3a3530,#151312 50%,#6d6258)"><div class="date-badge"><b>02</b><small>Aug</small></div></div>
  <h3 class="event-title">Jonas Vennberg Koncert</h3>
  <p class="event-desc">Lorem ipsum dolor sit consectetur adipiscing lorem ispum.</p>
  <div class="event-foot"><span class="btn-event">Se Event</span><span class="likes"><svg width="18" height="15" viewBox="0 0 18 15"><path d="M9 15L1.5 7.5A4 4 0 0 1 9 2.5a4 4 0 0 1 7.5 5z" fill="#bbb"/></svg>03</span></div>
</article>
<article class="event-card" style="left:590px;top:523px">
  <div class="event-photo" role="img" aria-label="Foto: taler ved en talerstol" style="background:linear-gradient(135deg,#f2f3f5,#c7ccd3 55%,#2d3550)"><div class="date-badge"><b>02</b><small>Aug</small></div></div>
  <h3 class="event-title">Jonas Vennberg Koncert</h3>
  <p class="event-desc">Lorem ipsum dolor sit consectetur adipiscing lorem ispum.</p>
  <div class="event-foot"><span class="btn-event">Se Event</span><span class="likes"><svg width="18" height="15" viewBox="0 0 18 15"><path d="M9 15L1.5 7.5A4 4 0 0 1 9 2.5a4 4 0 0 1 7.5 5z" fill="#bbb"/></svg>03</span></div>
</article>

<!-- row 3 -->
<article class="event-card" style="left:124px;top:768px">
  <div class="event-photo" role="img" aria-label="Foto: travl gågade om aftenen" style="background:linear-gradient(135deg,#5a6f8c,#8a6a4a 50%,#3a2a20)"><div class="date-badge"><b>02</b><small>Aug</small></div></div>
  <h3 class="event-title">Jonas Vennberg Koncert</h3>
  <p class="event-desc">Lorem ipsum dolor sit consectetur adipiscing lorem ispum.</p>
  <div class="event-foot"><span class="btn-event">Se Event</span><span class="likes"><svg width="18" height="15" viewBox="0 0 18 15"><path d="M9 15L1.5 7.5A4 4 0 0 1 9 2.5a4 4 0 0 1 7.5 5z" fill="#bbb"/></svg>03</span></div>
</article>
<article class="event-card" style="left:357px;top:768px">
  <div class="event-photo" role="img" aria-label="Foto: venner der fester" style="background:linear-gradient(135deg,#2a2218,#b88a5a 50%,#e8c9a0)"><div class="date-badge"><b>02</b><small>Aug</small></div></div>
  <h3 class="event-title">Jonas Vennberg Koncert</h3>
  <p class="event-desc">Lorem ipsum dolor sit consectetur adipiscing lorem ispum.</p>
  <div class="event-foot"><span class="btn-event">Se Event</span><span class="likes"><svg width="18" height="15" viewBox="0 0 18 15"><path d="M9 15L1.5 7.5A4 4 0 0 1 9 2.5a4 4 0 0 1 7.5 5z" fill="#bbb"/></svg>03</span></div>
</article>
<article class="event-card" style="left:590px;top:768px">
  <div class="event-photo" role="img" aria-label="Foto: gæster i en bar med blåt lys" style="background:linear-gradient(135deg,#1a2a8a,#c06040 50%,#2a50c0)"><div class="date-badge"><b>02</b><small>Aug</small></div></div>
  <h3 class="event-title">Jonas Vennberg Koncert</h3>
  <p class="event-desc">Lorem ipsum dolor sit consectetur adipiscing lorem ispum.</p>
  <div class="event-foot"><span class="btn-event">Se Event</span><span class="likes"><svg width="18" height="15" viewBox="0 0 18 15"><path d="M9 15L1.5 7.5A4 4 0 0 1 9 2.5a4 4 0 0 1 7.5 5z" fill="#bbb"/></svg>03</span></div>
</article>

<div class="divider"></div>

<!-- favorites -->
<h2 class="section-title" style="left:847px;top:223px">MINE FAVORITTER</h2>
<div class="fav" style="top:275px">
  <div class="thumb" role="img" aria-label="Foto: glade festdeltagere" style="background:linear-gradient(135deg,#c0203a,#e8a070 60%,#f1d9b0)"></div>
  <div class="name hot">Jonas Vennberg Koncert</div><div class="date">02 - Aug - 2014</div>
</div>
<div class="fav" style="top:369px">
  <div class="thumb" role="img" aria-label="Foto: catwalk med fotografer" style="background:linear-gradient(135deg,#3a3530,#151312 55%,#6d6258)"></div>
  <div class="name">Lorem ipsum dolor sit amet,</div><div class="date">02 - Aug - 2014</div>
</div>
<div class="fav" style="top:463px">
  <div class="thumb" role="img" aria-label="Foto: taler ved en talerstol" style="background:linear-gradient(135deg,#f2f3f5,#c7ccd3 60%,#2d3550)"></div>
  <div class="name">Jonas Vennberg Koncert</div><div class="date">02 - Aug - 2014</div>
</div>
<div class="fav" style="top:557px">
  <div class="thumb" role="img" aria-label="Foto: gæster i en bar med blåt lys" style="background:linear-gradient(135deg,#1a2a8a,#c06040 55%,#2a50c0)"></div>
  <div class="name">Jonas Vennberg Koncert</div><div class="date">02 - Aug - 2014</div>
</div>
<div class="fav" style="top:651px;border-bottom:0">
  <div class="thumb" role="img" aria-label="Foto: dansende silhuetter i solnedgang" style="background:linear-gradient(180deg,#f0c040,#d07010 55%,#1a1208)"></div>
  <div class="name">Jonas Vennberg Koncert</div><div class="date">02 - Aug - 2014</div>
</div>

<!-- newsletter -->
<section class="newsletter">
  <div class="nl-head"><svg width="28" height="26" viewBox="0 0 28 26"><path d="M2 11l12-9 12 9v14H2z" fill="#1b2245"/><rect x="6" y="4" width="16" height="13" fill="#fff" stroke="#1b2245"/><circle cx="14" cy="10" r="3.5" fill="none" stroke="#1b2245" stroke-width="1.5"/><path d="M2 11l12 8 12-8" fill="none" stroke="#fff" stroke-width="1.5"/></svg>NYHRDSBREV</div>
  <p class="nl-text">Lorem ipsum dolor sit amet, etur adipiscing elit. Nunc laoreet etus non tortor varius, et rhon magna posuere.</p>
  <form class="nl-form"><input type="email" placeholder="Email"><button type="button" aria-label="Tilmeld"><svg width="12" height="12" viewBox="0 0 12 12"><path d="M1 1l10 5-10 5 2-5z" fill="#fff"/></svg></button></form>
  <div class="nl-stripe"></div>
</section>

<footer class="site-footer">
  <nav class="foot-nav"><a class="active">Alle</a><span class="sep">/</span><a>Musik</a><span class="sep">/</span><a>Sport</a><span class="sep">/</span><a>Teater</a><span class="sep">/</span><a>Udstilling</a><span class="sep">/</span><a>Elder</a><span class="sep">/</span><a>Born</a><span class="sep">/</span><a>Motin</a><span class="sep">/</span><a>Diverse</a></nav>
  <div class="copy">© 2014, KULTRA. All rights reserved</div>
</footer>

</div>
</body>
</html>
```